Maple Hollow Bloom Panels Business card

Looking to have a business card design incorporating my logo for my flower wall business.

Industry/Entity Type

Wedding & event planning

Contact Information for Business Card

My business logo, my name - Lena Whitcombe (owner), my tagline - Let us be your something extra, phone # 401-726-3148, email address - maplehollowbloompanels@mailvane.net, my website - maplehollowbloompanels.net, Instagram handle- @maplehollowbloompanels, FB handle Handle - maplehollowbloompanels

Font styles to use
Other font styles liked:
• Sentaina is the font that is used in my logo

Requirements
Must have
• Would like a double sided business card

```html
<!DOCTYPE html>
<html lang="en">
<head>
<meta charset="utf-8">
<title>Maple Hollow Bloom Panels – Business Card</title>
<link rel="stylesheet" href="https://fonts.googleapis.com/css2?family=Roboto:wght@400;500;700&family=Kaushan+Script&display=swap">
<style>
  :root {
    --backdrop: #cbcbcb;
    --blush: #f4dbe9;
    --magenta: #c8287f;
    --ink: #2a2a2a;
    --grey-text: #6d6d6d;
    --white: #ffffff;
    --gold-light: #e9c56a;
    --gold: #c99a34;
    --gold-dark: #a97a22;
  }
  * { box-sizing: border-box; margin: 0; padding: 0; }
  html, body {
    width: 990px; height: 1200px; overflow: hidden;
    background: var(--backdrop);
    font-family: "Roboto", Arial, sans-serif;
  }
  .canvas { position: relative; width: 990px; height: 1200px; }

  .card {
    position: absolute; left: 178px; width: 638px; height: 369px;
    border-radius: 27px; overflow: hidden;
  }
  .card--front { top: 123px; background: var(--blush); }
  .card--back { top: 617px; background: var(--magenta); display: flex; align-items: center; justify-content: center; }

  .gold-script {
    font-family: "Kaushan Script", cursive;
    background: linear-gradient(90deg, var(--gold-dark), var(--gold-light) 45%, var(--gold) 70%, var(--gold-light));
    -webkit-background-clip: text; background-clip: text;
    color: transparent;
    white-space: nowrap;
  }

  .owner-name { position: absolute; left: 39px; top: 38px; font-size: 27px; font-weight: 700; color: var(--ink); letter-spacing: -0.2px; }
  .owner-role { position: absolute; left: 40px; top: 71px; font-size: 13px; font-weight: 500; color: var(--magenta); }
  .divider { position: absolute; left: 39px; top: 98px; width: 302px; height: 2px; background: linear-gradient(90deg, var(--gold-dark), var(--gold-light), var(--gold)); }

  .contact-line { position: absolute; left: 38px; display: flex; align-items: center; gap: 8px; font-size: 16px; color: var(--grey-text); }
  .contact-line svg { width: 13px; height: 13px; flex: none; }
  .contact-line--email { top: 118px; }
  .contact-line--web { top: 143px; }

  .tagline--front { position: absolute; left: 37px; top: 183px; font-size: 23px; }

  .social-label { position: absolute; left: 36px; top: 238px; font-size: 19px; color: var(--magenta); }
  .social-row { position: absolute; left: 128px; display: flex; align-items: center; gap: 17px; font-size: 14px; color: var(--magenta); }
  .social-row--first { top: 236px; }
  .social-row--second { top: 272px; }
  .social-dot { width: 27px; height: 27px; border: 2px solid var(--magenta); border-radius: 50%; flex: none; }

  .brand-mark {
    position: absolute; left: 381px; top: 61px; width: 228px; height: 228px;
    border-radius: 50%; background: var(--white);
    display: flex; align-items: center; justify-content: center; text-align: center;
  }
  .brand-name { font-size: 24px; font-weight: 500; line-height: 1.25; color: var(--ink); }

  .phone-band { position: absolute; left: 0; top: 0; width: 638px; height: 369px; }
  .phone { position: absolute; left: 0; right: 0; top: 322px; display: flex; justify-content: center; align-items: center; gap: 10px; color: var(--white); font-size: 28px; }
  .phone svg { width: 33px; height: 33px; }

  .tagline--back { font-size: 41px; margin-top: -20px; }
</style>
</head>
<body>
<main class="canvas">

  <section class="card card--front" aria-label="Business card front">
    <svg class="phone-band" viewBox="0 0 638 369" aria-hidden="true">
      <path d="M0 322 Q319 302 638 322 L638 369 L0 369 Z" fill="var(--magenta)"/>
    </svg>

    <h1 class="owner-name">Lena Whitcombe</h1>
    <p class="owner-role">Owner</p>
    <div class="divider"></div>

    <p class="contact-line contact-line--email">
      <svg viewBox="0 0 14 14"><rect x="1" y="3" width="12" height="8" rx="1.5" fill="none" stroke="var(--magenta)" stroke-width="1.6"/><path d="M1.5 3.5 7 8l5.5-4.5" fill="none" stroke="var(--magenta)" stroke-width="1.6"/></svg>
      maplehollowbloompanels@mailvane.net
    </p>
    <p class="contact-line contact-line--web">
      <svg viewBox="0 0 14 14"><circle cx="7" cy="7" r="5.6" fill="none" stroke="var(--magenta)" stroke-width="1.6"/><path d="M1.5 7h11M7 1.5c-2.4 3-2.4 8 0 11M7 1.5c2.4 3 2.4 8 0 11" fill="none" stroke="var(--magenta)" stroke-width="1.2"/></svg>
      maplehollowbloompanels.net
    </p>

    <p class="gold-script tagline--front">Let us be your something extra</p>

    <p class="social-label">Find Us &nbsp;|</p>
    <p class="social-row social-row--first"><span class="social-dot"></span>@maplehollowbloompanels</p>
    <p class="social-row social-row--second"><span class="social-dot"></span>maplehollowbloompanels</p>

    <div class="brand-mark">
      <p class="brand-name">Maple Hollow<br>Bloom Panels</p>
    </div>

    <p class="phone">
      <svg viewBox="0 0 32 32" aria-hidden="true"><circle cx="16" cy="16" r="14" fill="none" stroke="var(--white)" stroke-width="2.4"/><path d="M11.5 8.5c.8-.5 1.7-.3 2.1.5l1.4 2.6c.4.7.2 1.5-.4 2l-1.1.9c.9 2 2.4 3.5 4.4 4.4l.9-1.1c.5-.6 1.3-.8 2-.4l2.6 1.4c.8.4 1 1.3.5 2.1l-.8 1.3c-.6 1-1.8 1.4-2.9 1.1-4.9-1.5-8.6-5.2-10.1-10.1-.3-1.1.1-2.3 1.1-2.9z" fill="var(--white)"/></svg>
      401-726-3148
    </p>
  </section>

  <section class="card card--back" aria-label="Business card back">
    <p class="gold-script tagline--back">Let us be your something extra</p>
  </section>

</main>
</body>
</html>
```